Professional, Attractive, Simple Website Needed!!

We completed the design for our logo.

We need a website built out around this.

Here are a couple samples of how we want ours formatted.

http://brvntapower.com

http://www.halvorbeam.com/lp/free-quote?LeadSource=Search%20Engine&ProgramName=webquery&experience=qual&language=en&type=brd&gclid=Xq7RTPwmEYKDLAvUHbsNQkfPZrTcGwnJuoVbXeLqHmRYdAsWtPkMcNfBYgzTrUoQJhEdWvKpYaLsZbCmNDgQwTxAoKpXbT_qkR

http://morvalo.co

Reason: Extending this deadline due to our delay in providing designers with content for each page. This is coming in next 24 hours.

Reason: Due to scheduling conflicts and extended travel delays related to Puerto Rico, the deadline has been extended. Your patience is greatly appreciated.

Reason: Travel and scheduling conflicts have made it impossible to give this project the thorough review it deserves, therefore I am extending the deadline. Thank you for your patience!

Target Market(s)

Home Owners who earn 60k + household annually

Industry/Entity Type

It Professional

Coding

Coded - Design and coding required

Number of Pages Required

5+ page

Font styles to use
Serif

Colors
34a7d8
9bcb3c

Requirements
Must have
• Simple
• Lead form Entry (Ability for visitor to enter Name, number and address for a quote)
• Sleek Design
• Professional
• Testimonials
• Use color Scheme of Design Logo Attached
Nice to have
• Video when site starts
• Like this
• https://www.vidmarrow.com/watch?v=qT8mRpXw2Ka&feature=vidm.ro
Should not have
• Should not include Commercial solar
• Should not include wind power

```html
<!DOCTYPE html>
<html lang="en">
<head>
<meta charset="utf-8">
<title>Terra Sol Energy – Residential Solar</title>
<link href="https://fonts.googleapis.com/css2?family=Nunito:wght@300;400;600;700&display=swap" rel="stylesheet">
<style>
:root{
  --blue:#34a7d8;
  --green:#9bcb3c;
  --ink:#1d1d1f;
  --muted:#555;
  --hero:#12171d;
  --news:#1b221c;
  --testi:#111213;
  --footer:#14252e;
  --white:#fff;
}
*{margin:0;padding:0;box-sizing:border-box}
html,body{width:1200px;height:2293px;overflow:hidden}
body{position:relative;font-family:"Nunito",Arial,sans-serif;color:var(--ink);background:var(--white)}
.abs{position:absolute}
section,header,footer{position:absolute;left:0;width:1200px}

/* Hero */
.hero{top:0;height:453px;background:linear-gradient(115deg,#1d3347 0%,#223d56 35%,#0f151b 70%,#080a0c 100%)}
.social{display:flex;gap:14px;align-items:center}
.social span{width:13px;height:13px;border-radius:50%;border:1.5px solid var(--white);display:block}
.social span.ring{width:20px;height:20px;border-color:var(--blue)}
.hero .social{left:255px;top:44px}
.brand{display:flex;flex-direction:column;align-items:center;gap:6px;font-weight:700;letter-spacing:.5px}
.brand .dot{width:46px;height:46px;border-radius:50%;border:3px solid var(--blue)}
.hero .brand{left:500px;top:18px;width:200px;color:var(--green);font-size:18px}
.menu{left:930px;top:44px;width:21px}
.menu i{display:block;height:3px;background:var(--white);margin-bottom:4px}
.hero-copy{left:250px;top:195px;width:340px;color:var(--white)}
.hero-copy h1{font-weight:300;line-height:1}
.hero-copy h1 .l1{display:block;font-size:42px}
.hero-copy h1 .l2{display:block;font-size:56px;margin-top:2px}
.hero-copy p{font-size:10.5px;line-height:15px;margin-top:14px}
.quote-ring{left:615px;top:168px;width:340px;height:340px;z-index:2}
.quote-form{left:658px;top:243px;width:254px;z-index:3;text-align:center}
.quote-form h2{color:var(--blue);font-weight:400;font-size:18px;margin-bottom:14px}
.quote-form .field{height:27px;border:1px solid #555;border-radius:3px;margin:0 12px 8px;text-align:left;padding-left:10px;font-size:10px;line-height:25px;color:#ddd}
.quote-form .btn{margin:12px 12px 0;height:26px;border-radius:13px;background:var(--blue);color:var(--white);font-size:9.5px;font-weight:700;line-height:26px}

/* Steps */
.steps{top:453px;height:433px;background:var(--white)}
.section-title{text-align:center;font-weight:400;font-size:28px}
.steps .section-title{position:absolute;top:72px;width:100%}
.step{top:155px;width:196px;text-align:center}
.step svg{display:block;margin:0 auto}
.step h3{color:var(--blue);font-weight:400;font-size:14px;line-height:17px;margin-top:16px}
.step p{font-size:10.5px;line-height:13px;color:var(--muted);margin-top:6px}

/* News */
.news{top:886px;height:501px;background:linear-gradient(180deg,#161b1a,#24301f 60%,#151a14)}
.news .section-title{position:absolute;top:40px;width:100%;color:var(--white)}
.news .sub{position:absolute;top:77px;width:100%;text-align:center;color:var(--white);font-size:15px}
.card{top:123px;width:222px;color:var(--white)}
.card .photo{height:148px}
.card h3{color:var(--blue);font-weight:400;font-size:14px;margin-top:16px}
.card time{display:block;font-size:8.5px;margin-top:1px}
.card p{font-size:10px;line-height:13px;margin-top:12px}
.pill{display:inline-block;margin-top:14px;width:82px;height:26px;border-radius:13px;background:var(--blue);color:var(--white);font-size:8.5px;font-weight:700;text-align:center;line-height:26px}

/* Testimonials */
.testimonials{top:1387px;height:398px;background:var(--testi);color:var(--white);text-align:center}
.testimonials .section-title{position:absolute;top:126px;width:100%;font-size:26px}
.dashes{width:62px;border-top:2px dashed var(--blue)}
.testimonials .dashes{left:569px;top:180px}
.testimonials blockquote{position:absolute;left:360px;top:208px;width:480px;font-size:10.5px;line-height:16px}
.arrow{top:213px}
.client{left:528px;top:275px;display:flex;gap:16px;align-items:center;text-align:left}
.avatar{width:56px;height:56px;border-radius:6px;border:2px solid var(--white);background:linear-gradient(#8a6a50,#3f3026)}
.client b{display:block;font-size:11px}
.client small{font-size:8px;color:#ccc}

/* Listings */
.listings{top:1785px;height:120px;background:var(--white)}
.badge{top:44px;height:34px;background:#8d8d8d;border-radius:3px}

/* Footer */
.site-footer{top:1905px;height:388px;background:linear-gradient(180deg,#182b34,#10202a);color:var(--white)}
.site-footer .brand{left:500px;top:22px;width:200px;color:var(--white);font-size:17px}
.foot-links{left:250px;top:128px;font-size:10.5px}
.foot-links h4,.newsletter h4{font-size:12px;font-weight:700;margin-bottom:14px}
.foot-links li{list-style:none;margin-bottom:5px}
.contact{left:450px;top:158px;width:300px;text-align:center;font-size:10.5px;line-height:19px}
.site-footer .d1{left:569px;top:135px}
.site-footer .d2{left:569px;top:248px}
.newsletter{left:750px;top:128px;width:201px;text-align:right;font-size:10.5px;line-height:14px}
.newsletter .input{margin-top:14px;height:25px;border:1px solid #667;border-radius:3px;position:relative;text-align:left;font-size:9.5px;line-height:23px;padding-left:8px}
.newsletter .go{position:absolute;right:3px;top:3px;width:17px;height:17px;background:var(--blue)}
.site-footer .social{left:533px;top:290px}
.copy{left:250px;top:358px;font-size:9px}
</style>
</head>
<body>

<header class="hero">
  <div class="social abs"><span></span><span class="ring"></span><span></span><span></span><span></span></div>
  <div class="brand abs"><span class="dot"></span>Terra Sol Energy</div>
  <div class="menu abs"><i></i><i></i><i></i></div>
  <div class="hero-copy abs">
    <h1><span class="l1">World Savings</span><span class="l2">Start Here.</span></h1>
    <p>Lorem Ipsum has been the industry's standard dummy text ever since the 1500s, when an unknown printer took a galley of type and scrambled it to make a type specimen book</p>
  </div>
</header>

<svg class="quote-ring abs" viewBox="0 0 340 340" aria-hidden="true">
  <circle cx="170" cy="170" r="160" fill="#0b0c0d"/>
  <path d="M12 150 A160 160 0 0 1 328 150" fill="none" stroke="#34a7d8" stroke-width="8"/>
  <path d="M328 150 A160 160 0 1 1 12 150" fill="none" stroke="#9bcb3c" stroke-width="8"/>
</svg>
<form class="quote-form abs">
  <h2>Ability for Visitor to Enter</h2>
  <div class="field">First Name</div>
  <div class="field">Phone</div>
  <div class="field">Address</div>
  <div class="btn">Get A Quote</div>
</form>

<section class="steps">
  <h2 class="section-title">Easy Steps to Going Solar</h2>
  <div class="step abs" style="left:210px">
    <svg width="96" height="96" viewBox="0 0 96 96"><path d="M8 48 A40 40 0 0 1 88 48" fill="none" stroke="#34a7d8" stroke-width="6"/><path d="M88 48 A40 40 0 0 1 8 48" fill="none" stroke="#9bcb3c" stroke-width="6"/><path d="M30 52 V44 A18 18 0 0 1 66 44 V52" fill="none" stroke="#34a7d8" stroke-width="5"/><rect x="26" y="48" width="10" height="16" rx="2" fill="#9bcb3c"/><rect x="60" y="48" width="10" height="16" rx="2" fill="#9bcb3c"/></svg>
    <h3>Speak to a<br>solar consultant</h3>
    <p>Lorem Ipsum is simply<br>dummy text of the printing</p>
  </div>
  <div class="step abs" style="left:406px">
    <svg width="96" height="96" viewBox="0 0 96 96"><path d="M8 48 A40 40 0 0 1 88 48" fill="none" stroke="#34a7d8" stroke-width="6"/><path d="M88 48 A40 40 0 0 1 8 48" fill="none" stroke="#9bcb3c" stroke-width="6"/><rect x="28" y="28" width="40" height="24" fill="#34a7d8"/><path d="M28 36H68M28 44H68M38 28V52M48 28V52M58 28V52" stroke="#fff" stroke-width="1.5"/><rect x="46" y="52" width="4" height="10" fill="#9bcb3c"/><rect x="36" y="62" width="24" height="4" fill="#9bcb3c"/></svg>
    <h3>We'll design your<br>solar panel system</h3>
    <p>Lorem Ipsum is simply<br>dummy text of the printing</p>
  </div>
  <div class="step abs" style="left:602px">
    <svg width="96" height="96" viewBox="0 0 96 96"><path d="M8 48 A40 40 0 0 1 88 48" fill="none" stroke="#34a7d8" stroke-width="6"/><path d="M88 48 A40 40 0 0 1 8 48" fill="none" stroke="#9bcb3c" stroke-width="6"/><rect x="28" y="30" width="40" height="34" rx="3" fill="none" stroke="#34a7d8" stroke-width="4"/><rect x="28" y="30" width="40" height="9" fill="#34a7d8"/><g fill="#9bcb3c"><rect x="34" y="44" width="6" height="5"/><rect x="45" y="44" width="6" height="5"/><rect x="56" y="44" width="6" height="5"/><rect x="34" y="53" width="6" height="5"/><rect x="45" y="53" width="6" height="5"/></g></svg>
    <h3>Schedule your<br>1 day install</h3>
    <p>Lorem Ipsum is simply<br>dummy text of the printing</p>
  </div>
  <div class="step abs" style="left:798px">
    <svg width="96" height="96" viewBox="0 0 96 96"><path d="M8 48 A40 40 0 0 1 88 48" fill="none" stroke="#34a7d8" stroke-width="6"/><path d="M88 48 A40 40 0 0 1 8 48" fill="none" stroke="#9bcb3c" stroke-width="6"/><path d="M52 24 L34 52 H48 L42 72 L62 42 H48 Z" fill="#34a7d8"/></svg>
    <h3>Start saving on your<br>electricity bill</h3>
    <p style="margin-top:1px">Lorem Ipsum is simply<br>dummy text of the printing</p>
  </div>
</section>

<section class="news" role="img" aria-label="Dimmed photo of a countryside house with solar panels behind the news section">
  <h2 class="section-title">Stay Up To Date</h2>
  <div class="sub">Recent News</div>
  <article class="card abs" style="left:250px">
    <div class="photo" role="img" aria-label="Close-up photo of blue solar panels" style="background:linear-gradient(135deg,#7fa2e0,#2c4fb5 55%,#1a2f80)"></div>
    <h3>Lorem Ipsum</h3><time>August 29, 2017</time>
    <p>Lorem Ipsum has been the industry's standard dummy text ever since the 1500s, when an unknown printer took a galley of type and scrambled it to make a type specimen book.</p>
    <span class="pill">Read More</span>
  </article>
  <article class="card abs" style="left:489px">
    <div class="photo" role="img" aria-label="Photo of the Earth seen from space" style="background:radial-gradient(circle at 45% 50%,#c9d1d4,#6f8a86 40%,#2e4a63 70%,#10203a)"></div>
    <h3>Lorem Ipsum</h3><time>August 29, 2017</time>
    <p>Lorem Ipsum has been the industry's standard dummy text ever since the 1500s, when an unknown printer took a galley of type and scrambled it to make a type specimen book.</p>
    <span class="pill">Read More</span>
  </article>
  <article class="card abs" style="left:729px">
    <div class="photo" role="img" aria-label="Photo of solar panels on a building roof against blue sky" style="background:linear-gradient(180deg,#b9e1f2 0%,#d8eef6 45%,#cfd3d5 55%,#9ea3a6 100%)"></div>
    <h3>Lorem Ipsum</h3><time>August 29, 2017</time>
    <p>Lorem Ipsum has been the industry's standard dummy text ever since the 1500s, when an unknown printer took a galley of type and scrambled it to make a type specimen book.</p>
    <span class="pill">Read More</span>
  </article>
</section>

<section class="testimonials">
  <svg class="abs" style="left:564px;top:34px" width="72" height="72" viewBox="0 0 72 72" aria-hidden="true"><path d="M5 36 A31 31 0 0 1 67 36" fill="none" stroke="#34a7d8" stroke-width="4"/><path d="M67 36 A31 31 0 0 1 5 36" fill="none" stroke="#9bcb3c" stroke-width="4"/><path d="M25 44 V36 Q25 28 32 26 M40 44 V36 Q40 28 47 26" fill="none" stroke="#fff" stroke-width="5"/></svg>
  <h2 class="section-title">Testimonials</h2>
  <div class="dashes abs"></div>
  <blockquote>Lorem Ipsum is simply dummy text of the printing and typesetting industry. Lorem Ipsum has been the industry's standard dummy text ever since the 1500s, when an unknown printer took a galley of type and scrambled it to make a type specimen book.</blockquote>
  <svg class="arrow abs" style="left:250px" width="16" height="26" viewBox="0 0 16 26" aria-label="Previous"><path d="M13 2 L3 13 L13 24" fill="none" stroke="#fff" stroke-width="3"/></svg>
  <svg class="arrow abs" style="left:934px" width="16" height="26" viewBox="0 0 16 26" aria-label="Next"><path d="M3 2 L13 13 L3 24" fill="none" stroke="#fff" stroke-width="3"/></svg>
  <div class="client abs">
    <div class="avatar" role="img" aria-label="Client portrait"></div>
    <div><b>Sam Rowan</b><small>new client</small></div>
  </div>
</section>

<section class="listings" aria-label="Listings and accreditations">
  <div class="badge abs" style="left:308px;width:88px;border-radius:17px"></div>
  <div class="badge abs" style="left:446px;width:60px"></div>
  <div class="badge abs" style="left:556px;width:90px"></div>
  <div class="badge abs" style="left:688px;width:76px;background:#555"></div>
  <div class="badge abs" style="left:832px;width:38px;border-radius:50%;height:38px;top:42px"></div>
</section>

<footer class="site-footer">
  <div class="brand abs"><span class="dot" style="border-color:#fff"></span>Terra Sol Energy</div>
  <div class="foot-links abs">
    <h4>Link</h4>
    <ul><li>-&nbsp; Home</li><li>-&nbsp; About Us</li><li>-&nbsp; Events</li><li>-&nbsp; Testimonials</li><li>-&nbsp; Contact us</li></ul>
  </div>
  <div class="dashes abs d1"></div>
  <address class="contact abs" style="font-style:normal">ABC, Street City, 12345 City<br>(+00 000 000 0000) &nbsp;-&nbsp; (+00 000 000 0000)<br>hello@terrasolenergy.com<br>www.terrasolenergy.com</address>
  <div class="dashes abs d2"></div>
  <div class="newsletter abs">
    <h4>Newsletter</h4>
    <p>Lorem Ipsum is simply dummy text of the printing and typesetting industry.</p>
    <div class="input">Enter your email address<span class="go"></span></div>
  </div>
  <div class="social abs"><span></span><span class="ring"></span><span></span><span></span><span></span></div>
  <p class="copy abs">© Copyright 2017 Terra Sol Energy. All Rights Reserved.</p>
</footer>

</body>
</html>
```